Business Card Design Project

I have a two letter domain name qo.com.au (lower case font please). I want a business card, cum logo that is die cut (around the qo segment at least) that fits standard business card size.
qo is all about what 'I am' - a journalist, blogger, analyst, commentator. My mantra is "I wander so qo'.
The reverse of the card only needs my name Lon Fitch, email lon@qo.com.au and mobile +61 400 555 817
Target Market(s)
Mainly people that will use my professional writing services and suppliers that will provide product for review
Industry/Entity Type
Business
Requirements
Must have
- One side is qo.com.au (hint - the .com.au can be vertical or horizontal to fit - the qo should be as large as possible).
The other requires large size font name, email and phone details (so no one needs glasses to read it).
The die cut can be just to highlight the qo segment - need not be around the whole card.
Font used in the past was Belwe (old style - very much like the i used in the information symbol).
Colours - no preference - prefer two colour to process colour but can also be an outline font instead of solid colour.

```html
<!DOCTYPE html>
<html lang="en">
<head>
<meta charset="utf-8">
<title>Lon Fitch — Business Card</title>
<link rel="stylesheet" href="https://fonts.googleapis.com/css2?family=Archivo:ital,wght@1,700;1,800&display=swap">
<style>
  :root {
    --paper: #ffffff;
    --bubble: #f5f17c;
    --ink: #231f20;
  }
  html, body {
    margin: 0;
    padding: 0;
    width: 1200px;
    height: 667px;
    overflow: hidden;
    background: var(--paper);
  }
  .card {
    position: relative;
    width: 1200px;
    height: 667px;
    background: var(--paper);
  }
  .card__art {
    display: block;
    width: 1200px;
    height: 667px;
  }
  .backdrop { fill: var(--bubble); }
  .name {
    font-family: "Archivo", "Helvetica Neue", Arial, sans-serif;
    font-style: italic;
    font-weight: 800;
    font-size: 247px;
    fill: var(--ink);
  }
  .contact {
    font-family: "Archivo", "Helvetica Neue", Arial, sans-serif;
    font-style: italic;
    font-weight: 700;
    fill: var(--ink);
  }
  .contact--email { font-size: 66px; }
  .contact--phone { font-size: 60px; }
</style>
</head>
<body>
  <main class="card">
    <svg class="card__art" viewBox="0 0 1200 667" xmlns="http://www.w3.org/2000/svg" aria-labelledby="card-title">
      <title id="card-title">Lon Fitch, lon@qo.com.au, +61 400 555 817</title>

      <rect class="backdrop" x="6" y="84" width="1194" height="500" rx="250" ry="250"
            role="img" aria-label="Cluster of overlapping yellow speech bubbles behind the contact details"/>

      <g class="identity">
        <text class="name name--first" x="66" y="336" textLength="368" lengthAdjust="spacingAndGlyphs">LON</text>
        <text class="name name--last" x="74" y="525" textLength="615" lengthAdjust="spacingAndGlyphs">FITCH</text>
      </g>

      <g class="contact-details">
        <text class="contact contact--email" x="446" y="330" textLength="488" lengthAdjust="spacingAndGlyphs">lon@qo.com.au</text>
        <text class="contact contact--phone" x="708" y="401" textLength="440" lengthAdjust="spacingAndGlyphs">+61 400 555 817</text>
      </g>
    </svg>
  </main>
</body>
</html>
```